Unique Extrior cleaning Logo

We need a new business card design, i would like to use our existing logo (attached).
Our logo on the left & a unique graphic design on the right of either a man holding a pressure washer gun & hose with a thumbs up or an image portraying dirt melting off a building or the two incorperated together, or something similar that represents exterior cleaning in progress, an image that shows/explains that we are exterior cleaners/pressure washers. Has to incorporate the google & facebook symbol perhaps in the bottom corners of the business card.
Existing business symbol on the back of the card with some blank lines for space to hand write quotes or job notes.
Industry/Entity Type
Exterior Cleaning
Contact Information for Business Card
Business mobile No. to be prominent (0487 214 960) Services provided listed as dot points. -Soft Washing -Pressure Washing - Solar Panel Cleaning - All General Exterior Cleaning. Email listed in fineprint (enquiries@brightvalewashcrew.com.au). Owner Operator - Desmond Fairlie (this should also be added somewhere prominent). Residential & Comercial Cleaning.
Colors
Designer to choose colors to be used in the design.
Look and feel

```html
<!DOCTYPE html>
<html lang="en">
<head>
<meta charset="utf-8">
<title>Brightvale Wash Crew – Business Card</title>
<link href="https://fonts.googleapis.com/css2?family=Roboto:wght@400;500;700&display=swap" rel="stylesheet">
<style>
  :root {
    --stage: #3a3a3a;
    --card: #141414;
    --card-edge: #4a63b0;
    --accent: #4a63b0;
    --ink: #f2f2f2;
    --ink-soft: #d8d8d8;
  }
  * { box-sizing: border-box; margin: 0; padding: 0; }
  html, body {
    width: 1200px; height: 801px; overflow: hidden;
    background: var(--stage);
    font-family: "Roboto", Arial, sans-serif;
  }
  .sheet {
    width: 1200px; height: 801px;
    display: flex; align-items: center; justify-content: center; gap: 40px;
  }
  .card {
    position: relative;
    width: 540px; height: 309px;
    background: var(--card);
    border: 1.5px solid var(--card-edge);
    border-radius: 16px;
    overflow: hidden;
    color: var(--ink);
  }

  /* Front */
  .brand {
    position: absolute; left: 30px; top: 0; bottom: 0; width: 180px;
    display: flex; align-items: center; gap: 10px;
  }
  .brand-mark { width: 16px; height: 16px; background: var(--accent); flex: none; }
  .brand-name {
    font-weight: 700; font-size: 19px; line-height: 1.15;
    letter-spacing: 0.04em; text-transform: uppercase; color: var(--ink);
  }
  .divider {
    position: absolute; left: 220px; top: 74px; height: 158px;
    border-left: 1px solid var(--accent);
  }
  .contact {
    position: absolute; left: 244px; top: 76px; right: 14px;
    font-size: 12.5px; color: var(--ink-soft); line-height: 1.5;
  }
  .contact-name {
    font-weight: 700; font-size: 23px; color: var(--accent);
    text-transform: uppercase; letter-spacing: 0.01em; line-height: 1.1;
  }
  .contact-role { font-size: 14px; color: var(--ink); margin-bottom: 8px; }
  .contact-line { display: flex; align-items: center; gap: 7px; white-space: nowrap; }
  .contact-line svg { width: 11px; height: 11px; flex: none; fill: var(--accent); }
  .contact-phone { color: var(--accent); font-weight: 700; font-size: 15px; }
  .contact-email { font-size: 11.5px; }
  .contact-sector { margin-top: 4px; font-size: 13px; color: var(--ink); }

  /* Back */
  .back-pattern {
    position: absolute; inset: 0;
    background:
      linear-gradient(200deg, rgba(70,70,70,0.55) 0%, rgba(20,20,20,0) 45%),
      linear-gradient(20deg, #050505 0%, #1b1b1b 55%, #2c2c2c 100%);
  }
  .back-brand {
    position: absolute; right: 40px; top: 120px;
    display: flex; align-items: center; gap: 8px;
  }
  .back-brand .brand-mark { width: 12px; height: 12px; }
  .back-brand .brand-name { font-size: 15px; }
  .services {
    position: absolute; right: 40px; top: 168px;
    text-align: right; font-size: 15px; line-height: 1.55; color: var(--ink);
  }
  .services .dot { color: var(--accent); margin: 0 4px; }
</style>
</head>
<body>
<main class="sheet">
  <section class="card card-front">
    <div class="brand">
      <span class="brand-mark"></span>
      <span class="brand-name">Brightvale<br>Wash Crew</span>
    </div>
    <div class="divider"></div>
    <div class="contact">
      <p class="contact-name">Desmond Fairlie</p>
      <p class="contact-role">Owner Operator</p>
      <p class="contact-line contact-phone">
        <svg viewBox="0 0 24 24" aria-hidden="true"><path d="M6.6 10.8a15 15 0 0 0 6.6 6.6l2.2-2.2a1 1 0 0 1 1-.25 11.4 11.4 0 0 0 3.6.57 1 1 0 0 1 1 1V20a1 1 0 0 1-1 1A17 17 0 0 1 3 4a1 1 0 0 1 1-1h3.5a1 1 0 0 1 1 1c0 1.25.2 2.45.57 3.57a1 1 0 0 1-.25 1z"/></svg>
        0487 214 960
      </p>
      <p class="contact-line contact-email">
        <svg viewBox="0 0 24 24" aria-hidden="true"><path d="M2 5h20v14H2z M2 5l10 8 10-8" /></svg>
        enquiries@brightvalewashcrew.com.au
      </p>
      <p class="contact-line">
        <svg viewBox="0 0 24 24" aria-hidden="true"><circle cx="12" cy="12" r="10"/></svg>
        www.brightvalewashcrew.com.au
      </p>
      <p class="contact-sector">Residential &amp; Comercial Cleaning</p>
    </div>
  </section>

  <section class="card card-back">
    <div class="back-pattern" role="img" aria-label="Dark repeating pattern of slanted tiles in black and grey"></div>
    <div class="back-brand">
      <span class="brand-mark"></span>
      <span class="brand-name">Brightvale Wash Crew</span>
    </div>
    <p class="services">
      Soft Washing<span class="dot">•</span>Pressure Washing<br>
      Solar Panel Cleaning<span class="dot">•</span>All General Exterior Cleaning
    </p>
  </section>
</main>
</body>
</html>
```